Business card for Northland's Blue Wagon.

Good day i am looking for a business card design for my business.
The name of the business is Northland's Blue Wagon. It is a van rental business that provides a driver and helper to the customer. Customer have use to van for small moves, studio or 1 bedroom, Moving furniture like couch or kitchen cabinets.
We are available evenings, weekends and holidays.
the means to contact us is by phone at 628-947-2071; By emails at Oakridge@northlandsbluewagon.net; or by social media, Linkwall and Snapgrid.
You can see attached pictures of the van and or logo.

```html
<!DOCTYPE html>
<html lang="en">
<head>
<meta charset="UTF-8">
<title>Northland's Blue Wagon — Business Card</title>
<link rel="stylesheet" href="https://fonts.googleapis.com/css2?family=Merriweather:wght@400;700&display=swap">
<style>
  :root {
    --page-bg: #e4e4e6;
    --card-bg: #ffffff;
    --brand-red: #d2232a;
    --ink: #1c1c1c;
    --ink-soft: #4a4a4a;
    --shadow: rgba(0, 0, 0, 0.18);
  }
  * { box-sizing: border-box; margin: 0; padding: 0; }
  html, body {
    width: 1200px;
    height: 900px;
    overflow: hidden;
    background: var(--page-bg);
    font-family: "Merriweather", Georgia, serif;
  }
  .sheet {
    position: relative;
    width: 1200px;
    height: 900px;
  }
  .card {
    position: absolute;
    left: 270px;
    width: 660px;
    height: 377px;
    background: var(--card-bg);
    box-shadow: 0 6px 18px var(--shadow);
  }
  .card--front { top: 50px; }
  .card--back { top: 473px; }

  /* brand mark: plain circle + name */
  .brand {
    position: absolute;
    display: flex;
    align-items: center;
    gap: 14px;
    color: var(--brand-red);
    font-weight: 700;
  }
  .brand__dot {
    flex: none;
    border-radius: 50%;
    background: var(--brand-red);
  }
  .brand__name { white-space: nowrap; }
  .brand__line { display: block; }

  .card--front .brand {
    left: 50%;
    top: 50%;
    transform: translate(-50%, -50%);
    font-size: 26px;
  }
  .card--front .brand__dot { width: 34px; height: 34px; }

  .card--back .brand {
    left: 40px;
    top: 175px;
    font-size: 19px;
    line-height: 1.35;
  }
  .card--back .brand__dot { width: 28px; height: 28px; }

  .back-info {
    position: absolute;
    right: 34px;
    top: 40px;
    width: 370px;
    text-align: right;
  }
  .tagline {
    color: var(--brand-red);
    font-weight: 700;
    font-size: 20px;
    white-space: nowrap;
  }
  .socials {
    margin-top: 62px;
    display: flex;
    justify-content: flex-end;
    gap: 16px;
    font-size: 13px;
    color: var(--ink-soft);
  }
  .socials span::before {
    content: "";
    display: inline-block;
    width: 10px;
    height: 10px;
    margin-right: 6px;
    border-radius: 50%;
    background: var(--brand-red);
  }
  .contact {
    margin-top: 12px;
    list-style: none;
    color: var(--ink-soft);
  }
  .contact li {
    display: flex;
    justify-content: flex-end;
    align-items: center;
    gap: 10px;
    margin-top: 8px;
    white-space: nowrap;
  }
  .contact__phone { font-size: 20px; }
  .contact__email { font-size: 16px; }
  .contact svg { width: 20px; height: 20px; flex: none; }
  .divider {
    margin-top: 14px;
    height: 2px;
    background: var(--brand-red);
  }
  .services {
    margin-top: 12px;
    font-weight: 700;
    font-size: 14px;
    color: var(--ink);
    white-space: nowrap;
  }
</style>
</head>
<body>
<main class="sheet">
  <section class="card card--front" aria-label="Card front">
    <div class="brand">
      <span class="brand__dot"></span>
      <span class="brand__name">Northland's Blue Wagon</span>
    </div>
  </section>

  <section class="card card--back" aria-label="Card back">
    <div class="brand">
      <span class="brand__dot"></span>
      <span class="brand__name">
        <span class="brand__line">Northland's</span>
        <span class="brand__line">Blue Wagon</span>
      </span>
    </div>

    <div class="back-info">
      <p class="tagline">Small Moves, Big Help</p>
      <div class="socials">
        <span>Linkwall</span>
        <span>Snapgrid</span>
      </div>
      <ul class="contact">
        <li class="contact__phone">
          628-947-2071
          <svg viewBox="0 0 24 24" aria-hidden="true"><path fill="var(--brand-red)" d="M6.6 10.8a15 15 0 0 0 6.6 6.6l2.2-2.2a1 1 0 0 1 1-.25 11.4 11.4 0 0 0 3.6.57 1 1 0 0 1 1 1V20a1 1 0 0 1-1 1A17 17 0 0 1 3 4a1 1 0 0 1 1-1h3.5a1 1 0 0 1 1 1c0 1.25.2 2.45.57 3.57a1 1 0 0 1-.25 1z"/></svg>
        </li>
        <li class="contact__email">
          Oakridge@northlandsbluewagon.net
          <svg viewBox="0 0 24 24" aria-hidden="true"><rect x="2" y="5" width="20" height="14" rx="1.5" fill="var(--brand-red)"/><path d="M3 6.5l9 6.5 9-6.5" fill="none" stroke="#fff" stroke-width="1.6"/></svg>
        </li>
      </ul>
      <div class="divider"></div>
      <p class="services">Van Rental With Driver / Evening And Weekends</p>
    </div>
  </section>
</main>
</body>
</html>
```